Financial investment calculator report for real estae - layout & design

I am looking to Create a web report utilizing the attached information. It is an investment calculator report that will be customized report based on an online calculator. Therefore the report will need to be designed in a manner that a backend developer will be able to build off of.

The report will need to be web based but also printed in PDF format. The report will need to include the calculation format as well as be templeted to add a report user unique profile information like Headshot, Business Logo, Name, Telephone number, email etc.

The report should be modern and clean and easy to read and use a modern clean template design. It should be able to be easily color customized by the end user to produce templets in Red, Blue, Green, and Greyscale.

The report should be no more than 3 pages total with out breaking up the sections.

Section One - Cover sheet including agent bio info, Report Title and property address (both prominent), 400 Character space for property description, Property Pictures (3), and a google Maps integration image showing property location, It should also have room for about 100 words for a text disclaimer. (I will provide text soon)

Section Two - Inputs from the calculator

Section 3 - The Four Benefits & Rates of Return

Once I have a completed/approved form I will have about a half dozen forms/reports that will need to be laid out with a similar aesthetic.

Feel free to ask me any questions. Thank You
Tobin
Updates

Target Market(s)

This report will be produced by real estate agents forvtheir investor clients. It should denote professionalism

Font styles to use
Sans Serif

Colors
0054AA
0677BA
7BADD7
CADEEF
E8F1F8
00AB8E
00BBA5
67D7C9
C6EFE9
E9F9F6
EB3D1F
EC4F4E
F09395
F8D3D4
FCEDEE

```html
<!DOCTYPE html>
<html lang="en">
<head>
<meta charset="utf-8">
<title>418 Larkspur – Investment Report</title>
<link href="https://fonts.googleapis.com/css2?family=Lato:wght@400;700&display=swap" rel="stylesheet">
<style>
:root{
  --accent:#2a0ff0;
  --ink:#111;
  --muted:#555;
  --rule:#dcdcdc;
  --panel:#fafafa;
  --band:#efefef;
  --neg:#ec4f4e;
}
*{box-sizing:border-box;margin:0;padding:0}
html,body{width:849px;height:1200px;overflow:hidden;background:#fff}
body{position:relative;font-family:'Lato',sans-serif;color:var(--ink)}
.abs{position:absolute}
.logo-mark{left:45px;top:15px;width:70px;height:70px;border-radius:50%;background:#000}
.agency-name{left:136px;top:42px;font-size:15px;font-weight:700;letter-spacing:.2px}
.agent{right:202px;top:29px;text-align:right}
.agent-name{font-size:16px;font-weight:700;color:var(--accent);letter-spacing:.2px}
.agent-line{font-size:11px;margin-top:6px;display:flex;justify-content:flex-end;align-items:center;gap:14px}
.headshot{left:682px;top:30px;width:114px;height:122px;border-radius:8px;background:linear-gradient(160deg,#8fb3b8,#3b4a3c 60%,#2b3a2d);box-shadow:0 2px 8px rgba(0,0,0,.2)}
.rule-grey{left:37px;top:113px;width:775px;height:1px;background:var(--rule)}
.rule-accent{left:37px;top:112px;width:273px;height:2px;background:var(--accent)}
.title{left:38px;top:122px;font-size:23px;font-weight:700}
.subtitle{left:38px;top:153px;font-size:10px;font-weight:700}
.location{left:37px;top:174px;font-size:10px;font-weight:700;display:flex;align-items:center;gap:9px}
.card{left:38px;top:265px;width:775px;height:800px;background:var(--panel);border-radius:8px;box-shadow:0 1px 8px rgba(0,0,0,.12)}
.section{position:absolute;left:54px;width:736px}
.band{height:29px;background:var(--band);border-radius:5px;display:flex;align-items:center;padding:0 13px 0 11px;font-size:12px}
.band .dot{width:4px;height:4px;border-radius:50%;background:var(--accent);margin-right:16px}
.band .label{font-weight:500}
.band .note{font-size:8px}
.rows{margin-left:42px}
.row{position:relative;height:20.4px;border-bottom:1px solid var(--rule);font-size:8px;color:var(--muted)}
.row span{position:absolute;top:6px}
.row .r{right:0}
.c1{left:177px}.c2{left:321px}.c3{left:519px}
.totalbar{position:relative;border-top:2px solid var(--accent);margin-top:-1px;height:26px}
.totalbar span{position:absolute;top:6px;font-size:11.5px;font-weight:700}
.totalbar .r{right:0;top:5px;font-size:12px}
.subhead{font-size:11.5px;font-weight:700;margin:10px 0 3px}
.footer{left:38px;top:1178px;width:775px;display:flex;justify-content:space-between;font-size:8px;color:var(--muted)}
</style>
</head>
<body>
<div class="abs logo-mark"></div>
<div class="abs agency-name">AGENCYNAME <span style="font-weight:400">HERE</span></div>

<div class="abs agent">
  <div class="agent-name">GREG TOBIN</div>
  <div class="agent-line">
    <svg width="10" height="10" viewBox="0 0 24 24" fill="none" stroke="#111" stroke-width="2"><path d="M5 3h4l2 5-3 2a12 12 0 0 0 6 6l2-3 5 2v4a2 2 0 0 1-2 2A18 18 0 0 1 3 5a2 2 0 0 1 2-2z"/></svg>
    (555) 214-0387
  </div>
  <div class="agent-line">greg.tobin@example.com</div>
</div>
<div class="abs headshot" role="img" aria-label="Agent headshot photo"></div>

<div class="abs rule-grey"></div>
<div class="abs rule-accent"></div>
<div class="abs title">418 LARKSPUR</div>
<div class="abs subtitle">15-Plex of 1bd/1bth Apartments</div>
<div class="abs location">
  <svg width="8" height="11" viewBox="0 0 24 32"><path d="M12 0a12 12 0 0 0-12 12c0 9 12 20 12 20s12-11 12-20A12 12 0 0 0 12 0zm0 17a5 5 0 1 1 0-10 5 5 0 0 1 0 10z" fill="#111"/></svg>
  15-Plex of 1bd/1bth Apartments
</div>

<div class="abs card"></div>

<section class="section" style="top:278px">
  <div class="band"><i class="dot"></i><span class="label">PROPERTY ADDRESS:</span><span class="note" style="margin-left:auto">418 Larkspur Ave, Fairview, KS 66999</span></div>
  <div class="rows">
    <div class="row"><span>Financing</span><span class="c2">20% Down</span><span class="r">20 Year Conventional</span></div>
    <div class="row"><span>Purchase Price</span><span class="r">$1.690.000</span></div>
    <div class="row"><span>Down Payment (Cash Invested)</span><span class="c2">20% of purchase price</span><span class="r">$338.000</span></div>
    <div class="row"><span>Amount Financed</span><span class="r">$1.352.000</span></div>
    <div class="row"><span>Needed Capital Improvements Est</span><span class="r">$0</span></div>
    <div class="row"><span>Est. Closing Costs</span><span class="r">$3.000</span></div>
    <div class="row"><span>CASH Invested (Down Pmt. + Closing Costs)</span><span class="r">$341.000</span></div>
    <div class="totalbar"><span style="left:0">Rate: 7%</span><span class="c1">Term: 20 years</span><span class="c2">Monthly P&amp;I:</span><span class="r">$10.482</span></div>
  </div>
</section>

<section class="section" style="top:497px">
  <div class="band"><i class="dot"></i><span class="label">DEPRICIATION (FIRST YEAR): (ASSUMES 80%/20%)</span><span class="note abs" style="left:363px">Est. Value</span><span class="note abs" style="left:561px">Yearly Rate</span></div>
  <div class="rows">
    <div class="row"><span>Land Cost</span><span class="c1">0 Year</span><span class="c2">$338.000</span><span class="c3">0%</span><span class="r">$0</span></div>
    <div class="row"><span>Personal Property Cost</span><span class="c1">5 Years</span><span class="c2">$45.000</span><span class="c3">20%</span><span class="r">$9.000</span></div>
    <div class="row"><span>Building Cost</span><span class="c1">27.5 Years</span><span class="c2">$1.262.000</span><span class="c3">3.48%</span><span class="r">$43.918</span></div>
    <div class="row"><span>Land Improvement Cost</span><span class="c1">15 Years</span><span class="c2">$45.000</span><span class="c3">5%</span><span class="r">$2.250</span></div>
    <div class="totalbar" style="margin-left:320px;border-top-width:2px"><span style="left:1px">Total Depreciation:</span><span class="r">$55.168</span></div>
  </div>
</section>

<section class="section" style="top:649px">
  <div class="band"><i class="dot"></i><span class="label">INCOME:</span></div>
  <div class="rows">
    <div class="row"><span>Annual Rent</span><span class="r">$170.000</span></div>
    <div class="row"><span>Other Income</span><span class="r">$0</span></div>
    <div class="row"><span>Less Vacancy</span><span class="c2">est. 5% of annual rent</span><span class="r" style="color:var(--neg)">-$0</span></div>
    <div class="totalbar" style="margin-left:320px"><span style="left:1px">Gross Operating Income:</span><span class="r">$170.000</span></div>
  </div>
</section>

<section class="section" style="top:782px">
  <div class="band"><i class="dot"></i><span class="label">EXPENSES:</span></div>
  <div class="rows">
    <div class="row"><span>Real Estate Tax</span><span class="r">$27.439</span></div>
    <div class="row"><span>Insurance</span><span class="c2">est.</span><span class="r">$3.492</span></div>
    <div class="row"><span>Association Dues/HOA's</span><span class="r">$0</span></div>
    <div class="row"><span>Management</span><span class="c2">0%</span><span class="r">$0</span></div>
    <div class="row"><span>Utilities</span><span class="r">$9.192</span></div>
    <div class="subhead">PROPERTY ADDRESS</div>
    <div class="row"><span>Advertising</span><span class="r">$170.000</span></div>
    <div class="row"><span>Maintnence</span><span class="c2">est.</span><span class="r">$40.123</span></div>
    <div class="row"><span>Miscellaneous1</span><span class="c2">est.</span><span class="r">$129.877</span></div>
    <div class="row"><span>Miscellaneous2</span><span class="c2">est.</span><span class="r">$125.784</span></div>
    <div class="totalbar" style="margin-left:320px"><span style="left:1px">Total Expenses:</span><span class="r">$4.092</span></div>
  </div>
</section>

<footer class="abs footer">
  <span>418 Larkspur, REF #52k3190 by Northgate Realty | Report at www.example.com. June 26th, 2023</span>
  <span>Page 2/3</span>
</footer>
</body>
</html>
```